We need a professional looking 4 x 9 Rack Card

I need a 2 sided 4 x 9 rack card for my boat charter business. Please see website (www.tidelarkcruise.com) and attached files for the type of look and artwork we've used thus far. And see some attached examples that competitors are using. Please don't copy these ideas...I just sent them so you can understand what others are doing and what I think looks good and what looks bad. I'm looking for you to provide your best ideas.

Target Market(s)

Hotel and resort tourists who visit Clearwater Beach and surrounding areas.

Industry/Entity Type

Business

Colors

Designer to choose colors to be used in the design.

Requirements
Must have
• The top 1/4 of the front side is most important to have strong headline/artwork. Need powerful imagery. I will pay for images you need. Please review website to gain understanding of what we are selling. www.tidelarkcruise.com. I'd like designers to offer their best messaging ideas based on their impression of what will be appealing to target market. To help, please know that our customers want to go boating but instead of renting a boat themselves, they hire us to take them out. Some of the favorite things we do are to go dolphin watching, sunset cruises, and taking them to private, secluded beaches where they can walk and look for seashells. I want it to be a simple design, not cluttered.
Nice to have
• website (www.tidelarkcruise.com), phone (813)-555-2741, email address (info@tidelarkcruise.com), tripadvisor logo, facebook logo, youtube logo, instagram logo,
Should not have
• Do not need mailing address on the card.

```html
<!DOCTYPE html>
<html lang="en">
<head>
<meta charset="utf-8">
<title>Tidelark Cruise – Rack Card</title>
<link href="https://fonts.googleapis.com/css2?family=Ubuntu:wght@500;700&family=Source+Sans+3:wght@600;700&display=swap" rel="stylesheet">
<style>
  :root {
    --page: #eceae6;
    --blue: #1a63b0;
    --blue-deep: #165aa3;
    --blue-light: #e9f1f9;
    --orange: #f05a22;
    --amber: #f7941d;
    --red: #e3262e;
    --navy: #1c3a8c;
    --ink: #141414;
    --white: #ffffff;
    --grey: #8a8f96;
  }
  html, body { margin: 0; padding: 0; overflow: hidden; }
  body {
    width: 1200px; height: 1200px;
    background: var(--page);
    position: relative;
  }
  .rack-card {
    position: absolute;
    top: 78px;
    width: 455px; height: 1023px;
    box-shadow: 0 14px 24px rgba(0,0,0,.25);
  }
  .rack-card--front { left: 86px; }
  .rack-card--back { left: 649px; }
  .rack-card svg { display: block; width: 455px; height: 1023px; }

  .brand-name { font-family: "Ubuntu", sans-serif; font-weight: 500; font-size: 40px; }
  .brand-tag { font-family: "Source Sans 3", sans-serif; font-weight: 600; font-size: 17px; }
  .headline { font-family: "Source Sans 3", sans-serif; font-weight: 700; font-size: 78px; fill: var(--white); letter-spacing: -1px; }
  .ribbon-label { font-family: "Ubuntu", sans-serif; font-weight: 700; font-size: 26px; fill: var(--white); }
  .offer-text { font-family: "Ubuntu", sans-serif; font-weight: 700; font-size: 23px; fill: var(--white); }
  .activity-label { font-family: "Ubuntu", sans-serif; font-weight: 500; font-size: 10.5px; fill: var(--white); }
  .plan-title { font-family: "Source Sans 3", sans-serif; font-weight: 700; font-size: 24px; fill: var(--white); }
  .plan-hours { font-family: "Source Sans 3", sans-serif; font-weight: 700; font-size: 20px; fill: var(--white); }
  .tagline { font-family: "Source Sans 3", sans-serif; font-weight: 700; font-size: 20px; fill: var(--white); }
  .tagline-sub { font-family: "Source Sans 3", sans-serif; font-weight: 600; font-size: 14.5px; fill: var(--white); }
  .cta { font-family: "Source Sans 3", sans-serif; font-weight: 700; font-size: 21px; fill: var(--white); }
  .cta-phone { font-family: "Source Sans 3", sans-serif; font-weight: 700; font-size: 40px; fill: var(--white); }
  .web { font-family: "Ubuntu", sans-serif; font-weight: 500; font-size: 19px; fill: var(--white); }
</style>
</head>
<body>

<!-- Front side -->
<section class="rack-card rack-card--front">
  <svg viewBox="0 0 455 1023" xmlns="http://www.w3.org/2000/svg">
    <defs>
      <linearGradient id="frontPhotoTone" x1="0" y1="0" x2="0" y2="1">
        <stop offset="0" stop-color="#f4efe4"/>
        <stop offset="0.22" stop-color="#c9b9a4"/>
        <stop offset="0.3" stop-color="#8d8d92"/>
        <stop offset="0.55" stop-color="#6e6a74"/>
        <stop offset="1" stop-color="#5b4338"/>
      </linearGradient>
    </defs>

    <rect class="hero-photo" x="0" y="0" width="455" height="790" fill="url(#frontPhotoTone)"
          role="img" aria-label="Photo of relaxed feet resting on a boat deck at sunset over the water"/>

    <g class="brand">
      <circle cx="86" cy="58" r="9" fill="var(--ink)"/>
      <text class="brand-name" x="106" y="72" fill="var(--ink)">Tidelark Cruise</text>
      <text class="brand-tag" x="227" y="124" text-anchor="middle" fill="var(--ink)">DOLPHIN TOURS AND BOAT CRUISES</text>
    </g>

    <text class="headline" x="36" y="494">LET'S GO</text>
    <text class="headline" x="36" y="586">BOATING!</text>

    <g class="lower-panel">
      <polygon points="0,682 455,722 455,1023 0,1023" fill="var(--blue)"/>
      <polygon points="105,690 455,724 455,730 105,697" fill="var(--grey)"/>
      <polygon points="160,684 455,712 455,734 160,700" fill="var(--orange)"/>

      <polygon points="0,739 211,758 211,826 0,818" fill="var(--orange)"/>
      <polygon points="211,751 455,778 455,858 211,842" fill="var(--red)"/>
      <polygon points="211,826 243,830 243,848 211,842" fill="#b51c22"/>
      <polygon points="0,843 243,866 243,950 0,926" fill="var(--red)"/>
      <polygon points="211,856 455,880 455,962 211,938" fill="var(--orange)"/>

      <text class="ribbon-label" x="22" y="792" transform="rotate(4 22 792)">Dolphin tours</text>
      <text class="ribbon-label" x="246" y="806" transform="rotate(5 246 806)">Sunset cruises</text>
      <text class="ribbon-label" x="36" y="897" transform="rotate(5 36 897)">Beach walks</text>
      <text class="ribbon-label" x="258" y="910" transform="rotate(5 258 910)">Sightseeing!</text>
    </g>

    <polygon class="footer-band" points="34,992 418,992 455,1023 0,1023" fill="var(--amber)"/>
    <text class="web" x="227" y="1015" text-anchor="middle">www.tidelarkcruise.com</text>
  </svg>
</section>

<!-- Back side -->
<section class="rack-card rack-card--back">
  <svg viewBox="0 0 455 1023" xmlns="http://www.w3.org/2000/svg">
    <defs>
      <linearGradient id="backSky" x1="0" y1="0" x2="0" y2="1">
        <stop offset="0" stop-color="var(--blue-light)"/>
        <stop offset="0.08" stop-color="#dbe7f4"/>
        <stop offset="0.26" stop-color="#2f7cc6"/>
        <stop offset="0.45" stop-color="var(--blue)"/>
        <stop offset="1" stop-color="var(--blue-deep)"/>
      </linearGradient>
      <linearGradient id="backPhotoTone" x1="0" y1="0" x2="0" y2="1">
        <stop offset="0" stop-color="#cfe4f4"/>
        <stop offset="0.45" stop-color="#9cc3df"/>
        <stop offset="0.7" stop-color="#c9c7c2"/>
        <stop offset="1" stop-color="#e9ecee"/>
      </linearGradient>
    </defs>

    <rect x="0" y="0" width="455" height="1023" fill="url(#backSky)"/>

    <g class="brand">
      <circle cx="131" cy="44" r="9" fill="var(--ink)"/>
      <text class="brand-name" x="150" y="58" fill="var(--ink)" font-size="36">Tidelark Cruise</text>
      <text class="brand-tag" x="227" y="95" text-anchor="middle" fill="var(--navy)">DOLPHIN TOURS AND BOAT CRUISES</text>
    </g>

    <g class="offer-banner">
      <polygon points="34,162 433,114 427,155 34,206" fill="var(--amber)"/>
      <polygon points="23,206 431,155 422,198 23,242" fill="var(--orange)"/>
      <text class="offer-text" x="51" y="196" transform="rotate(-6.8 51 196)">Rent the 24' Baylander deck boat</text>
      <text class="offer-text" x="55" y="232" transform="rotate(-6.8 55 232)">with a captain as your guide.</text>
    </g>

    <g class="activities">
      <polygon points="0,262 91,248 91,334 0,342" fill="var(--red)"/>
      <polygon points="91,256 182,244 182,330 91,338" fill="var(--orange)"/>
      <polygon points="182,254 273,242 273,328 182,336" fill="var(--red)"/>
      <polygon points="273,252 364,240 364,326 273,334" fill="var(--orange)"/>
      <polygon points="364,250 455,238 455,324 364,332" fill="var(--red)"/>
      <g fill="none" stroke="var(--white)" stroke-width="2.5">
        <circle cx="49" cy="289" r="10"/>
        <circle cx="140" cy="284" r="10"/>
        <circle cx="229" cy="282" r="10"/>
        <circle cx="322" cy="280" r="10"/>
        <circle cx="410" cy="278" r="10"/>
      </g>
      <text class="activity-label" x="49" y="318" text-anchor="middle">Sightseeing</text>
      <text class="activity-label" x="138" y="314" text-anchor="middle">Cruising</text>
      <text class="activity-label" x="229" y="316" text-anchor="middle">Dolphins</text>
      <text class="activity-label" x="322" y="315" text-anchor="middle">Skiing</text>
      <text class="activity-label" x="410" y="314" text-anchor="middle">Snorkeling</text>
    </g>

    <g class="photo-frame">
      <polygon points="62,396 455,338 455,350 62,405" fill="var(--orange)"/>
      <polygon points="0,418 455,352 455,362 0,430" fill="var(--white)"/>
      <polygon points="0,430 455,368 455,562 0,611" fill="url(#backPhotoTone)"
               role="img" aria-label="Photo of a happy group waving from a deck boat on the bay"/>
      <polygon points="0,611 455,562 455,572 0,626" fill="var(--orange)"/>
      <polygon points="0,640 363,593 363,603 0,652" fill="var(--white)"/>
    </g>

    <g class="plan plan--half">
      <polygon points="37,662 181,662 199,700 181,718 37,718 30,700" fill="var(--red)"/>
      <polygon points="37,662 166,662 181,684 37,684" fill="var(--amber)"/>
      <polygon points="125,718 181,718 165,729 140,738 136,738 138,730" fill="var(--orange)"/>
      <text class="plan-title" x="110" y="683" text-anchor="middle">HALF DAY</text>
      <text class="plan-hours" x="110" y="709" text-anchor="middle">(4 hours)</text>
    </g>
    <g class="plan plan--full">
      <polygon points="246,662 390,662 408,700 390,718 246,718 239,700" fill="var(--red)"/>
      <polygon points="246,662 375,662 390,684 246,684" fill="var(--amber)"/>
      <polygon points="336,718 390,718 376,729 350,738 346,738 348,730" fill="var(--orange)"/>
      <text class="plan-title" x="319" y="683" text-anchor="middle">FULL DAY</text>
      <text class="plan-hours" x="319" y="709" text-anchor="middle">(8 hours)</text>
    </g>

    <g class="tagline-banner">
      <polygon points="367,792 383,781 383,795" fill="var(--amber)"/>
      <polygon points="36,795 431,792 431,826 36,826 16,811" fill="var(--amber)"/>
      <text class="tagline" x="227" y="818" text-anchor="middle">Personalize Your Day On The Water!</text>
      <text class="tagline-sub" x="227" y="853" text-anchor="middle">Dolphin tours, sunset cruises, beach walks and sightseeing!</text>
    </g>

    <g class="booking">
      <polygon points="41,875 409,875 377,963 73,963" fill="var(--orange)"/>
      <polygon points="46,879 403,879 373,959 77,959" fill="none" stroke="#ffd2bd" stroke-width="1.5"/>
      <text class="cta" x="227" y="904" text-anchor="middle">BOOK YOUR ADVENTURE TODAY!</text>
      <text class="cta-phone" x="227" y="948" text-anchor="middle">(813) 555-2741</text>
    </g>

    <polygon class="footer-band" points="34,992 418,992 455,1023 0,1023" fill="var(--amber)"/>
    <text class="web" x="227" y="1015" text-anchor="middle">www.tidelarkcruise.com</text>
  </svg>
</section>

</body>
</html>
```